Commercial wall and ceiling contractor needs website

Construction trade companies are notoriously behind the rest of the world when it comes to using current technology to run their businesses; we are not one of those companies. We are a walls and ceilings contractor using up to date communications technologies and applying them unlike any other in our trade. As simple as it sounds, and it really is that simple, it is still a new idea in the trade. We are moving our customers towards communicating with us through a single point of contact using text and email; we distribute information to the appropriate internal party on our end. We need a website that generally appears traditionally familiar to the visitor while also expresses a fresh new approach and edginess to the trade business.

Target Market(s)

General contractors looking to get a bit of background info before inviting us to bid on their projects. This is not a high traffic environment. Their subsequent site visits will be primarily for contact info.

Industry/Entity Type

Construction Company

Number of Pages Required

3 page

Font styles to use
Sans Serif

Requirements
Must have
• The file I uploaded named "kolsite.docx" does not have to appear on the site in the same manner in which appears in the document file; but the info contained within that document does need to be represented on the site.

```html
<!DOCTYPE html>
<html lang="en">
<head>
<meta charset="utf-8">
<title>Stratline Walls and Ceilings Ltd.</title>
<link rel="stylesheet" href="https://fonts.googleapis.com/css2?family=Nunito+Sans:wght@400;600;700;800&family=Open+Sans:wght@400&family=Cinzel:wght@600&display=swap">
<style>
  :root {
    --frame: #e6e6e6;
    --page: #ffffff;
    --ink: #111111;
    --nav: #555555;
    --body-text: #6b6b6b;
    --brand: #2f7a52;
    --icon: #8a8a8a;
    --icon-fill: #f1f1f1;
    --photo-shadow: rgba(0, 0, 0, 0.2);
    --photo-rim: #f4f4f4;
  }
  * { box-sizing: border-box; margin: 0; padding: 0; }
  html, body {
    width: 1023px;
    height: 1200px;
    overflow: hidden;
    background: var(--frame);
  }
  .page {
    position: absolute;
    left: 13px;
    top: 13px;
    width: 997px;
    height: 1174px;
    background: var(--page);
    font-family: "Open Sans", sans-serif;
  }
  .site-header { position: relative; height: 170px; }
  .brand {
    position: absolute;
    left: 50%;
    top: 54px;
    transform: translateX(-50%);
    display: flex;
    align-items: center;
    gap: 10px;
    font-family: "Nunito Sans", sans-serif;
    font-weight: 800;
    font-size: 22px;
    color: var(--brand);
    white-space: nowrap;
  }
  .brand-mark {
    width: 14px;
    height: 14px;
    background: var(--brand);
  }
  .social {
    position: absolute;
    right: 58px;
    top: 60px;
    display: flex;
    gap: 3px;
  }
  .social-link {
    width: 21px;
    height: 21px;
    border: 1.5px solid var(--icon);
    border-radius: 50%;
    background: var(--icon-fill);
    display: flex;
    align-items: center;
    justify-content: center;
  }
  .social-link::after {
    content: "";
    width: 7px;
    height: 7px;
    border-radius: 50%;
    background: var(--icon);
  }
  .main-nav {
    position: absolute;
    top: 144px;
    left: 0;
    right: 0;
    display: flex;
    justify-content: center;
    gap: 42px;
    font-family: "Nunito Sans", sans-serif;
    font-weight: 700;
    font-size: 13px;
    letter-spacing: 0.3px;
  }
  .main-nav a { color: var(--nav); text-decoration: none; }
  .main-nav a.current { color: var(--ink); }
  .hero {
    position: absolute;
    left: 76px;
    top: 174px;
    width: 846px;
    height: 430px;
    border: 3px solid var(--photo-rim);
    border-radius: 8px;
    background: linear-gradient(105deg, #8c8c8c 0%, #a7a7a7 30%, #6c6c6c 52%, #b9b9b9 68%, #e4e4e4 85%, #f2f2f2 100%);
    box-shadow: 0 12px 14px -8px var(--photo-shadow);
  }
  .section-title {
    position: absolute;
    top: 692px;
    left: 0;
    right: 0;
    text-align: center;
    font-family: "Nunito Sans", sans-serif;
    font-weight: 800;
    font-size: 19px;
    color: var(--ink);
    letter-spacing: 0.4px;
  }
  .projects {
    position: absolute;
    top: 751px;
    left: 76px;
    display: flex;
    gap: 18px;
  }
  .project { width: 270px; }
  .project-photo {
    height: 163px;
    border: 3px solid var(--photo-rim);
    border-radius: 8px;
    box-shadow: 0 10px 12px -8px var(--photo-shadow);
  }
  .photo-1 { background: radial-gradient(ellipse 45% 55% at 50% 70%, #3a3a3e 0%, #7d8088 55%, #dfe3ea 100%); }
  .photo-2 { background: linear-gradient(180deg, #e9e9e9 0%, #d2d0cc 40%, #77706a 65%, #a3876a 100%); }
  .photo-3 { background: linear-gradient(180deg, #cdd3dc 0%, #6e7a92 35%, #2f3a52 60%, #8c6a4b 100%); }
  .project-title {
    margin-top: 25px;
    font-family: "Cinzel", serif;
    font-weight: 600;
    font-size: 15px;
    color: var(--ink);
  }
  .project-text {
    margin-top: 14px;
    font-size: 11.6px;
    line-height: 16px;
    color: var(--body-text);
  }
  .more-link {
    display: block;
    margin-top: 32px;
    width: 20px;
    height: 20px;
  }
</style>
</head>
<body>
<div class="page">
  <header class="site-header">
    <div class="brand"><span class="brand-mark"></span>Stratline Walls and Ceilings Ltd.</div>
    <div class="social" aria-label="Social links">
      <span class="social-link" role="img" aria-label="Social network link"></span>
      <span class="social-link" role="img" aria-label="Social network link"></span>
      <span class="social-link" role="img" aria-label="Social network link"></span>
    </div>
    <nav class="main-nav">
      <a class="current" href="#">HOME</a>
      <a href="#">ABOUT US</a>
      <a href="#">SERVICES</a>
      <a href="#">PROJECTS</a>
      <a href="#">NEWS</a>
      <a href="#">CONTACT US</a>
    </nav>
  </header>

  <div class="hero" role="img" aria-label="Black and white photo of a modern atrium with angled walls, stairs and a glazed skylight"></div>

  <h2 class="section-title">LATEST PROJECTS</h2>

  <section class="projects">
    <article class="project">
      <div class="project-photo photo-1" role="img" aria-label="Photo of a white ceiling with a crystal chandelier"></div>
      <h3 class="project-title">Project #1</h3>
      <p class="project-text">Lorem ipsum dolor sit amet, consectetuer adipiscing elit, sed diam nonummy nibh euismod tincidunt ut laoreet dolore magna aliquam erat volutpat. Ut wisi enim ad minim veniam, quis nostrud exerci tation ullamcorper suscipit lobortis nisl ut aliquip ex ea commodo consequat.</p>
      <svg class="more-link" viewBox="0 0 20 20" aria-label="Read more"><circle cx="10" cy="10" r="9" fill="#9a9a9a" stroke="#cfcfcf" stroke-width="1.5"/><path d="M5.5 10h8M10.5 6.5 14 10l-3.5 3.5" stroke="#fff" stroke-width="1.8" fill="none" stroke-linecap="round" stroke-linejoin="round"/></svg>
    </article>
    <article class="project">
      <div class="project-photo photo-2" role="img" aria-label="Photo of an open plan kitchen and dining area"></div>
      <h3 class="project-title">Project #2</h3>
      <p class="project-text">Lorem ipsum dolor sit amet, consectetuer adipiscing elit, sed diam nonummy nibh euismod tincidunt ut laoreet dolore magna aliquam erat volutpat. Ut wisi enim ad minim veniam, quis nostrud exerci tation ullamcorper suscipit lobortis nisl ut aliquip ex ea commodo consequat.</p>
      <svg class="more-link" viewBox="0 0 20 20" aria-label="Read more"><circle cx="10" cy="10" r="9" fill="#9a9a9a" stroke="#cfcfcf" stroke-width="1.5"/><path d="M5.5 10h8M10.5 6.5 14 10l-3.5 3.5" stroke="#fff" stroke-width="1.8" fill="none" stroke-linecap="round" stroke-linejoin="round"/></svg>
    </article>
    <article class="project">
      <div class="project-photo photo-3" role="img" aria-label="Photo of a living room with navy walls, fireplace and ceiling fan"></div>
      <h3 class="project-title">Project #3</h3>
      <p class="project-text">Lorem ipsum dolor sit amet, consectetuer adipiscing elit, sed diam nonummy nibh euismod tincidunt ut laoreet dolore magna aliquam erat volutpat. Ut wisi enim ad minim veniam, quis nostrud exerci tation ullamcorper suscipit lobortis nisl ut aliquip ex ea commodo consequat.</p>
      <svg class="more-link" viewBox="0 0 20 20" aria-label="Read more"><circle cx="10" cy="10" r="9" fill="#9a9a9a" stroke="#cfcfcf" stroke-width="1.5"/><path d="M5.5 10h8M10.5 6.5 14 10l-3.5 3.5" stroke="#fff" stroke-width="1.8" fill="none" stroke-linecap="round" stroke-linejoin="round"/></svg>
    </article>
  </section>
</div>
</body>
</html>
```